DJ Equipment Rental (business card/packet folder/stationary)

Designers:
The address will not longer be included in any of these designs. Thanks!

Attention designers,
It was brought to my attention that my brief was too broad and VERY confusing :/. I truly apologize.

This is what I need:
*Front and back business cards.
*A packet folder (front and back) (The size big enough to hold the 8x11 sheets)
I really don't know he size.

*Letter head

I needs to be professional, elegant, and it needs to stand out. Corporate like.

Colors:
Deep Red, Black, Deep blue . Also, follow color scheme of current logo but get creative.

Company: Vinyl Crate Hire Co
Phone: 918.555.0142
Email: Rentals@VinylCrateHireCo.example
Web: www.VinylCrateHireCo.example (under construction)
Address: 4826 W. Alder Lane, Tulsa, OK 74100
Logo: Provided

Project Deadline Extended
Reason: Due to my poor explanation and description of the project, I'm extending the due date of this project.

Target Market(s)

This folder will have my information as a business and it will serve as a marketing material. The audience range age is 18-43.

Industry/Entity Type

Business

Requirements
Must have
• Follow the color scheme provide in the logo.

```html
<!DOCTYPE html>
<html lang="en">
<head>
<meta charset="utf-8">
<title>Vinyl Crate Hire Co — Stationery Set</title>
<link rel="stylesheet" href="https://fonts.googleapis.com/css2?family=Orbitron:wght@500;700&family=Open+Sans:wght@400;600&display=swap">
<style>
  :root {
    --canvas: #8c8c8c;
    --ink-black: #0d0d0d;
    --paper: #ffffff;
    --text-grey: #555555;
    --text-light: #e8e8e8;
    --brand-orange: #f26a21;
    --brand-amber: #f7b733;
    --brand-red: #b3122a;
    --brand-teal: #39b5c9;
    --shadow: 0 6px 14px rgba(0,0,0,0.35);
  }
  * { box-sizing: border-box; margin: 0; padding: 0; }
  html, body { width: 1200px; height: 1000px; overflow: hidden; }
  body {
    background: var(--canvas);
    font-family: "Open Sans", Arial, sans-serif;
    position: relative;
  }

  .brand-name {
    font-family: "Orbitron", "Arial Black", sans-serif;
    font-weight: 700;
    color: var(--paper);
    white-space: nowrap;
    letter-spacing: 0.5px;
  }

  .equalizer-strip {
    position: absolute;
    left: 0; right: 0; bottom: 0;
    background: linear-gradient(90deg, var(--brand-amber), var(--brand-orange) 20%, var(--brand-red) 45%, var(--brand-orange) 60%, var(--brand-teal) 80%, var(--brand-amber));
    opacity: 0.9;
  }

  .contact-list { list-style: none; }
  .contact-list li { display: flex; align-items: center; white-space: nowrap; }
  .contact-icon { flex: none; }

  /* Letterhead */
  .letterhead {
    position: absolute; left: 35px; top: 35px;
    width: 618px; height: 875px;
    background: var(--paper);
    box-shadow: var(--shadow);
  }
  .letterhead-header {
    height: 73px; background: var(--ink-black);
    position: relative;
  }
  .letterhead-header .brand-name { position: absolute; left: 38px; top: 30px; font-size: 14px; }
  .letterhead-header .contact-list {
    position: absolute; left: 400px; top: 17px;
    font-size: 9px; color: var(--text-light); line-height: 13.5px;
  }
  .letterhead-header .contact-icon { width: 8px; height: 8px; margin-right: 5px; }
  .letterhead .equalizer-strip { height: 20px; bottom: 2px; }

  /* Envelope */
  .envelope {
    position: absolute; left: 450px; top: 150px;
    width: 700px; height: 330px;
    background: var(--paper);
    box-shadow: var(--shadow);
  }
  .envelope-header {
    height: 108px; background: var(--ink-black); position: relative;
  }
  .envelope-header .brand-name { position: absolute; left: 38px; top: 62px; font-size: 14px; }
  .envelope .contact-list {
    position: absolute; left: 44px; top: 122px;
    font-size: 9px; color: var(--text-grey); line-height: 13px;
  }
  .envelope .contact-icon { width: 7px; height: 7px; margin-right: 5px; }
  .envelope .equalizer-strip { height: 22px; bottom: 4px; }

  /* Business cards */
  .business-card {
    position: absolute; left: 745px;
    width: 382px; height: 224px;
    background: var(--ink-black);
    box-shadow: var(--shadow);
    overflow: hidden;
  }
  .card-front { top: 495px; }
  .card-back { top: 745px; height: 225px; }

  .card-feature-panel {
    position: absolute; left: 0; top: 0; width: 112px; height: 224px;
    background: linear-gradient(160deg, var(--brand-amber), var(--brand-orange) 55%, #e2352a);
  }
  .card-holder { position: absolute; right: 34px; top: 30px; text-align: right; }
  .card-holder-name {
    font-family: "Orbitron", "Arial Black", sans-serif; font-weight: 500;
    font-size: 15px; color: var(--brand-orange); letter-spacing: 0.5px;
  }
  .card-holder-role { font-size: 10px; color: var(--text-light); margin-top: 1px; }
  .card-front .contact-list {
    position: absolute; left: 124px; top: 112px;
    font-size: 11px; color: var(--text-light); line-height: 15.5px;
  }
  .card-front .contact-icon { width: 9px; height: 9px; margin-right: 6px; }
  .card-front .equalizer-strip { left: 98px; height: 14px; bottom: 4px; }

  .card-back .brand-name {
    position: absolute; left: 0; right: 0; top: 100px;
    text-align: center; font-size: 17px;
  }
</style>
</head>
<body>

<svg width="0" height="0" style="position:absolute" aria-hidden="true">
  <defs>
    <symbol id="icon-phone" viewBox="0 0 10 10"><rect width="10" height="10" rx="1.5" fill="#f26a21"/><path d="M3 2.2 L4.3 2.2 L4.7 3.8 L3.9 4.4 Q4.6 5.7 5.7 6.2 L6.3 5.4 L7.8 5.8 L7.8 7.2 Q4.5 7.8 2.6 3.8 Z" fill="#fff"/></symbol>
    <symbol id="icon-mobile" viewBox="0 0 10 10"><rect width="10" height="10" rx="1.5" fill="#f26a21"/><rect x="3.2" y="1.8" width="3.6" height="6.4" rx="0.6" fill="#fff"/><rect x="3.8" y="2.6" width="2.4" height="4" fill="#f26a21"/></symbol>
    <symbol id="icon-mail" viewBox="0 0 10 10"><rect width="10" height="10" rx="1.5" fill="#f26a21"/><rect x="2" y="3" width="6" height="4" fill="#fff"/><path d="M2 3 L5 5.4 L8 3" stroke="#f26a21" stroke-width="0.7" fill="none"/></symbol>
    <symbol id="icon-web" viewBox="0 0 10 10"><rect width="10" height="10" rx="1.5" fill="#f26a21"/><circle cx="5" cy="5" r="2.8" fill="none" stroke="#fff" stroke-width="0.9"/><path d="M2.2 5 H7.8 M5 2.2 V7.8" stroke="#fff" stroke-width="0.6"/></symbol>
  </defs>
</svg>

<section class="letterhead" aria-label="Letterhead">
  <header class="letterhead-header">
    <div class="brand-name">Vinyl Crate Hire Co</div>
    <ul class="contact-list">
      <li><svg class="contact-icon"><use href="#icon-phone"/></svg>918.555.0142</li>
      <li><svg class="contact-icon"><use href="#icon-mail"/></svg>Rentals@VinylCrateHireCo.example</li>
      <li><svg class="contact-icon"><use href="#icon-web"/></svg>www.VinylCrateHireCo.example</li>
    </ul>
  </header>
  <div class="equalizer-strip" role="img" aria-label="Colourful equalizer bar pattern"></div>
</section>

<section class="envelope" aria-label="Envelope">
  <header class="envelope-header">
    <div class="brand-name">Vinyl Crate Hire Co</div>
  </header>
  <ul class="contact-list">
    <li><svg class="contact-icon"><use href="#icon-phone"/></svg>918.555.0142</li>
    <li><svg class="contact-icon"><use href="#icon-mail"/></svg>Rentals@VinylCrateHireCo.example</li>
    <li><svg class="contact-icon"><use href="#icon-web"/></svg>www.VinylCrateHireCo.example</li>
  </ul>
  <div class="equalizer-strip" role="img" aria-label="Colourful equalizer bar pattern"></div>
</section>

<section class="business-card card-front" aria-label="Business card front">
  <div class="card-feature-panel" role="img" aria-label="Large orange brand graphic"></div>
  <div class="card-holder">
    <div class="card-holder-name">Dana Whitfield</div>
    <div class="card-holder-role">Founder</div>
  </div>
  <ul class="contact-list">
    <li><svg class="contact-icon"><use href="#icon-mobile"/></svg>000.000.000</li>
    <li><svg class="contact-icon"><use href="#icon-phone"/></svg>918.555.0142</li>
    <li><svg class="contact-icon"><use href="#icon-mail"/></svg>Rentals@VinylCrateHireCo.example</li>
    <li><svg class="contact-icon"><use href="#icon-web"/></svg>www.VinylCrateHireCo.example</li>
  </ul>
  <div class="equalizer-strip" role="img" aria-label="Colourful equalizer bar pattern"></div>
</section>

<section class="business-card card-back" aria-label="Business card back">
  <div class="brand-name">Vinyl Crate Hire Co</div>
</section>

</body>
</html>
```